Speisekarten
Zielgruppe
Die Sola Brisa Kassel ist vorrangig in der hochwertigen Gastronomie und Hotellerie tätig. Unser Leitspruch: IMMER EINEN TICK MEHR ALS ERWARTET. MEHR QUALITÄT, MEHR VIELFALT, MEHR LEISTUNG, MEHR LEIDENSCHAFT IN JEDEM DETAIL.
Was dazu gehört: Eine vielseitige Genießerwelt, die ihresgleichen sucht: Zehn Event-Locations, drei Hotels, zwanzig Tagungsräume, sieben Restaurants, eine Eisbar, zwei Feinkostgeschäfte und einen eigenen Strandabschnitt an der Lahn dürfen wir zu uns zählen.
Ob tagen, erholen, feiern oder genießen, bei uns gibt es das Rundum-Paket.
Aufgabenstellung
Sehr hochwertiges Design einer Speisekarte für ein asiatisches Restaurant der Extraklasse.

```html
<!DOCTYPE html>
<html lang="de">
<head>
<meta charset="utf-8">
<title>Restaurant Suirin – Speisekarte</title>
<link href="https://fonts.googleapis.com/css2?family=Jost:wght@300;400&display=swap" rel="stylesheet">
<style>
:root{
  --ink:#1c1b1b;
  --cover:#242222;
  --red:#e8303a;
  --paper:#ffffff;
  --text:#444444;
  --muted:#8a8a8a;
  --rule:#b5b5b5;
  --bg:#ffffff;
}
*{box-sizing:border-box;margin:0;padding:0}
html,body{width:1200px;height:3107px;overflow:hidden;background:var(--bg)}
body{position:relative;font-family:"Jost",sans-serif;font-weight:300;color:var(--text)}

.page{position:absolute;width:585px;height:585px;background:var(--paper);box-shadow:4px 4px 6px rgba(0,0,0,.35)}
.spread{position:absolute;width:1170px;height:585px;box-shadow:4px 4px 6px rgba(0,0,0,.35);background:var(--paper);border:1px solid #cfcfcf}
.spread .page{box-shadow:none;top:0}
.spread .page.left{left:0}
.spread .page.right{left:585px;border-left:1px solid var(--rule)}

/* covers */
.cover{background:var(--cover);color:#fff}
.cover .band{position:absolute;top:0;width:33px;height:100%;background:var(--red)}
.front .band{left:0}
.back .band{right:0}
.front .brand{position:absolute;left:160px;top:240px;display:flex;align-items:center;gap:22px}
.brand-square{width:34px;height:34px;border:2px solid var(--red)}
.front .brand-name{font-size:64px;font-weight:400;letter-spacing:10px;color:#fff}

.back .info{position:absolute;left:0;right:34px;top:0;text-align:center}
.back .brand-name{position:absolute;left:0;right:0;top:270px;font-size:34px;font-weight:400;letter-spacing:8px;color:#fff}
.back .dots{position:absolute;left:50%;top:305px;width:130px;margin-left:-65px;border-top:2px dotted #fff}
.back address{position:absolute;left:0;right:0;top:326px;font-style:normal;font-size:14px;line-height:23px;letter-spacing:.5px;color:#e6e6e6}

/* title spread */
.title-block{position:absolute;left:0;right:0;top:215px;text-align:center;color:var(--ink)}
.title-block .brand-name{font-size:40px;font-weight:400;letter-spacing:10px}
.title-block h1{margin-top:20px;font-size:28px;font-weight:400;letter-spacing:1.5px}
.title-block .dots{width:130px;margin:10px auto 0;border-top:2px dotted var(--ink)}
.title-block .sub{margin-top:14px;font-size:15px;letter-spacing:.3px;color:#333}

.intro{position:absolute;left:0;right:0;top:172px;text-align:center}
.intro .dots{width:130px;margin:0 auto;border-top:2px dotted #333}
.intro p{width:200px;margin:12px auto 12px;font-size:14.5px;line-height:22.7px;color:#555}

/* photos */
.photo{position:absolute;width:418px;height:418px;left:83px;top:82px}
.photo .caption{position:absolute;font-size:5.5px;line-height:7px;color:#fff;letter-spacing:.2px}
.ramen{background:radial-gradient(circle at 48% 45%,#f2c14a 0 8%,#e8d9b8 9% 22%,#4d5a2e 34%,#1d1d1b 56%,#2a2420 62%,#9a6a45 78%,#c89568 100%)}
.ramen .caption{left:28px;bottom:22px}
.fish{background:radial-gradient(ellipse at 50% 55%,#d7b98a 0 20%,#c24a2c 32%,#e6e2de 52%,#f2efec 70%,#8a6a4e 100%)}
.fish .caption{right:52px;bottom:22px}
.thumb{position:absolute;top:384px;width:116px;height:116px}
.thumb.pork{left:220px;background:radial-gradient(circle at 45% 55%,#5a2a18 0 22%,#3f6b2a 34%,#eae6e2 55%,#f4f2f0 100%)}
.thumb.fish-small{left:344px;background:radial-gradient(ellipse at 50% 55%,#d7b98a 0 22%,#c24a2c 36%,#eeeae6 60%,#9a7a5c 100%)}

/* menu lists */
.section-title{position:absolute;top:80px;height:420px;display:flex;align-items:flex-start}
.section-title h2{writing-mode:vertical-rl;transform:rotate(180deg);font-size:27px;font-weight:400;letter-spacing:1.5px;color:var(--ink);height:180px;text-align:left}
.vrule{position:absolute;top:80px;height:422px;border-left:2px dotted #555}
.menu{position:absolute;left:219px;width:240px;list-style:none}
.menu li{position:absolute;left:0;width:240px}
.menu .row{display:flex;align-items:baseline;font-size:13px;letter-spacing:-.2px;color:#4a4a4a;line-height:14px}
.menu .leader{flex:1;margin:0 3px;border-bottom:1px dotted #888;transform:translateY(-3px)}
.menu .price{font-size:8px;font-weight:400}
.menu .desc{margin-top:2px;font-size:9.5px;line-height:12px;color:var(--muted);width:170px}
</style>
</head>
<body>

<!-- front cover -->
<section class="page cover front" style="left:592px;top:10px">
  <div class="band"></div>
  <div class="brand"><span class="brand-square"></span><span class="brand-name">SUIRIN</span></div>
</section>

<!-- title spread -->
<section class="spread" style="left:8px;top:633px">
  <div class="page left">
    <div class="title-block">
      <div class="brand-name">SUIRIN</div>
      <h1>ASIAN CUISINE</h1>
      <div class="dots"></div>
      <div class="sub">RESTAURANT SUIRIN</div>
    </div>
  </div>
  <div class="page right">
    <div class="intro">
      <div class="dots"></div>
      <p>Lorem ipsum dolor sit amet, consectetuer adipiscing elit, sed diam nonummy nibh euismod tincidunt ut laoreet dolore magna aliquam erat volutpat. Ut wisi enim ad minim veniam, quis nostrud exerci tation ullamcorper suscipit lobortis nisl ut aliq.</p>
      <div class="dots"></div>
    </div>
  </div>
</section>

<!-- starters spread -->
<section class="spread" style="left:8px;top:1257px">
  <div class="page left">
    <div class="photo ramen" role="img" aria-label="Ramen-Schale mit Ei, Nudeln, Pilzen und Essstäbchen">
      <div class="caption">SPEISENBEZEICHNUNG<br>JE NACH WUNSCH</div>
    </div>
  </div>
  <div class="page right">
    <div class="section-title" style="left:124px"><h2>VORSPEISEN</h2></div>
    <div class="vrule" style="left:192px"></div>
    <ul class="menu">
      <li style="top:85px"><div class="row">LOREM IPSUM<span class="leader"></span><span class="price">6.90</span></div><div class="desc">Lorem ipsum dolor sit amet</div></li>
      <li style="top:133px"><div class="row">LOREM IPSUM DOLOR<span class="leader"></span><span class="price">6.20</span></div><div class="desc">Ut wisi enim ad minim veniam, quis nostrud exerci tation ullamcorper</div></li>
      <li style="top:193px"><div class="row">LOREM IPSUM DOLOR<span class="leader"></span><span class="price">6.20</span></div><div class="desc">Ut wisi enim ad minim veniam, quis nostrud exerci tation ullamcorper</div></li>
      <li style="top:255px"><div class="row">LOREM IPSUM DOLOR<span class="leader"></span><span class="price">6.20</span></div><div class="desc">Ut wisi enim ad minim veniam, quis nostrud exerci tation ullamcorper</div></li>
      <li style="top:313px"><div class="row">LOREM IPSUM<span class="leader"></span><span class="price">6.90</span></div><div class="desc">Lorem ipsum dolor sit amet</div></li>
      <li style="top:359px"><div class="row">LOREM IPSUM<span class="leader"></span><span class="price">6.90</span></div><div class="desc">Ut wisi enim ad minim veniam, quis nostrud exerci tation</div></li>
      <li style="top:421px"><div class="row">LOREM IPSUM DOLOR<span class="leader"></span><span class="price">6.20</span></div><div class="desc">Ut wisi enim ad minim veniam, quis nostrud exerci tation ullamcorper</div></li>
      <li style="top:479px"><div class="row">LOREM IPSUM<span class="leader"></span><span class="price">6.90</span></div><div class="desc">Lorem ipsum dolor sit amet</div></li>
    </ul>
  </div>
</section>

<!-- main course spread -->
<section class="spread" style="left:6px;top:1880px">
  <div class="page left">
    <div class="section-title" style="left:122px"><h2>MAIN MENUES</h2></div>
    <div class="vrule" style="left:193px"></div>
    <ul class="menu">
      <li style="top:85px"><div class="row">LOREM IPSUM<span class="leader"></span><span class="price">18.90</span></div><div class="desc">Lorem ipsum dolor sit amet</div></li>
      <li style="top:134px"><div class="row">LOREM IPSUM DOLOR<span class="leader"></span><span class="price">18.90</span></div><div class="desc">Ut wisi enim ad minim veniam, quis nostrud exerci tation ullamcorper</div></li>
      <li style="top:197px"><div class="row">LOREM IPSUM DOLOR<span class="leader"></span><span class="price">18.90</span></div><div class="desc">Ut wisi enim ad minim veniam, quis nostrud exerci tation ullamcorper</div></li>
      <li style="top:260px"><div class="row">LOREM IPSUM DOLOR<span class="leader"></span><span class="price">18.90</span></div><div class="desc">Ut wisi enim ad minim veniam, quis nostrud exerci</div></li>
      <li style="top:323px"><div class="row">LOREM IPSUM DOLOR<span class="leader"></span><span class="price">18.90</span></div><div class="desc">Ut wisi enim ad minim veniam, quis nostrud exerci tation ullamcorper</div></li>
    </ul>
    <div class="thumb pork" role="img" aria-label="Geschmortes Fleisch auf grünem Gemüse"></div>
    <div class="thumb fish-small" role="img" aria-label="Gebratenes Fischfilet auf roter Sauce"></div>
  </div>
  <div class="page right">
    <div class="photo fish" role="img" aria-label="Gebratenes Fischfilet mit Kräutern auf roter Sauce">
      <div class="caption">SPEISENBEZEICHNUNG<br>JE NACH WUNSCH</div>
    </div>
  </div>
</section>

<!-- back cover -->
<section class="page cover back" style="left:591px;top:2509px">
  <div class="band"></div>
  <div class="info">
    <div class="brand-name">SUIRIN</div>
    <div class="dots"></div>
    <address>RESTAURANT SUIRIN<br>STRASSENNAME 00<br>00112 ORTSCHAFT</address>
  </div>
</section>

</body>
</html>
```